Business card and Stationery for Physical, Occulational, Speech therapy
Oak Harbor Rehabilitation
Business card and Stationery for Physical, Occulational, Speech therapy - Health
Creative Brief
Professional
M.K. Delgado
PT, MSR, CSCS
2187 Willow Lane Bayfield South Carolina 29471
mkdelgado1@inbox-example.com
www.oakharborrehabilitation-example.com
2 Logos will be up loaded, Please use either
something creative!
Xpert Xpert
Star Rating please.

```html
<!DOCTYPE html>
<html lang="en">
<head>
<meta charset="utf-8">
<title>Oak Harbor Rehabilitation — Business Card</title>
<link rel="stylesheet" href="https://fonts.googleapis.com/css2?family=Montserrat:wght@400;600;800&display=swap">
<style>
  :root {
    --canvas-bg: #d9d6d1;
    --card-black: #0b0b0b;
    --pattern-dark: #161616;
    --pattern-mid: #3a3a3a;
    --brand-green: #5fe01c;
    --band-teal: #2fc291;
    --band-teal-light: #4fd6a6;
    --text-light: #e8e8e8;
    --text-dim: #9a9a9a;
    --text-dark: #0d2a20;
  }
  * { box-sizing: border-box; margin: 0; padding: 0; }
  html, body { width: 1200px; height: 904px; overflow: hidden; }
  body {
    background: var(--canvas-bg);
    font-family: "Montserrat", sans-serif;
    position: relative;
  }
  .card {
    position: absolute;
    left: 250px;
    width: 700px;
    height: 400px;
    border-radius: 18px;
    overflow: hidden;
    background: var(--card-black);
    box-shadow: 0 6px 18px rgba(0,0,0,.25);
  }
  .card--back { top: 40px; }
  .card--front { top: 464px; }

  /* back */
  .back-pattern {
    position: absolute; inset: 0;
    background:
      radial-gradient(ellipse at 30% 40%, rgba(90,90,90,.55), transparent 60%),
      radial-gradient(ellipse at 75% 75%, rgba(70,70,70,.45), transparent 55%),
      linear-gradient(135deg, var(--pattern-mid), var(--pattern-dark));
  }
  .back-mark {
    position: absolute; left: 400px; top: 214px;
    display: flex; align-items: center; gap: 12px;
  }
  .back-mark__dot {
    width: 34px; height: 34px; border-radius: 50%;
    background: var(--brand-green);
  }
  .back-mark__url {
    font-size: 12px; color: var(--text-dim); letter-spacing: .3px;
  }

  /* front */
  .emblem {
    position: absolute; right: 40px; top: 78px;
    width: 230px; height: 230px; border-radius: 50%;
    background: radial-gradient(circle at 40% 40%, #74ea36, var(--brand-green) 70%);
  }
  .emblem::after {
    content: ""; position: absolute; inset: 22px; border-radius: 50%;
    background: var(--card-black);
  }
  .brand {
    position: absolute; left: 34px; top: 92px;
  }
  .brand__name {
    display: flex; align-items: center; gap: 10px;
    font-size: 30px; font-weight: 800; color: var(--brand-green);
    line-height: 1.05; width: 400px;
  }
  .brand__dot {
    flex: none; width: 24px; height: 24px; border-radius: 50%;
    background: var(--brand-green);
  }
  .brand__services {
    margin-top: 8px; font-size: 9px; font-weight: 600;
    letter-spacing: 1.6px; color: var(--band-teal-light);
  }
  .person {
    position: absolute; right: 40px; top: 34px; text-align: right;
  }
  .person__name { font-size: 16px; font-weight: 600; color: var(--brand-green); }
  .person__creds { font-size: 11px; color: var(--text-light); margin-top: 3px; }

  .address {
    position: absolute; left: 34px; top: 172px;
    font-size: 12.5px; line-height: 1.45; color: var(--text-light); font-style: normal;
  }
  .phones {
    position: absolute; left: 34px; top: 216px;
    list-style: none; font-size: 13px; line-height: 1.5; color: var(--text-light);
  }
  .phones li, .band li { display: flex; align-items: center; gap: 8px; }
  .icon { width: 12px; height: 12px; flex: none; }

  .band {
    position: absolute; left: 0; right: 0; top: 300px; height: 64px;
    background: linear-gradient(90deg, var(--band-teal) 0%, var(--band-teal-light) 100%);
    padding: 11px 34px;
    list-style: none; font-size: 12.5px; line-height: 1.6; color: var(--text-dark);
  }
</style>
</head>
<body>

<section class="card card--back" aria-label="Business card back">
  <div class="back-pattern" role="img" aria-label="Repeating tone-on-tone brand pattern"></div>
  <div class="back-mark">
    <span class="back-mark__dot"></span>
    <span class="back-mark__url">www.oakharborrehabilitation-example.com</span>
  </div>
</section>

<section class="card card--front" aria-label="Business card front">
  <div class="emblem" role="img" aria-label="Large brand emblem area"></div>

  <div class="person">
    <div class="person__name">M.K. Delgado</div>
    <div class="person__creds">PT, MSR, CSCS</div>
  </div>

  <div class="brand">
    <div class="brand__name"><span class="brand__dot"></span>Oak Harbor Rehabilitation</div>
    <div class="brand__services">PHYSICAL • OCCUPATIONAL • SPEECH</div>
  </div>

  <address class="address">
    2187 Willow Lane, Bayfield<br>South Carolina, 29471
  </address>

  <ul class="phones">
    <li><svg class="icon" viewBox="0 0 12 12"><path d="M2.5 1h2l1 2.5-1.3 1a6 6 0 0 0 3.3 3.3l1-1.3L11 7.5v2A1.5 1.5 0 0 1 9.5 11 8.5 8.5 0 0 1 1 2.5 1.5 1.5 0 0 1 2.5 1z" fill="var(--band-teal-light)"/></svg>555-204-7731</li>
    <li><svg class="icon" viewBox="0 0 12 12"><rect x="3" y="1" width="6" height="10" rx="1.2" fill="var(--band-teal-light)"/><rect x="4" y="2.2" width="4" height="6.5" fill="var(--card-black)"/></svg>555-204-7732</li>
    <li><svg class="icon" viewBox="0 0 12 12"><rect x="1" y="3" width="10" height="7" rx="1" fill="var(--band-teal-light)"/><rect x="3" y="1" width="6" height="3" fill="var(--band-teal-light)"/></svg>555-880-1146</li>
  </ul>

  <ul class="band">
    <li><svg class="icon" viewBox="0 0 12 12"><rect x="1" y="2.5" width="10" height="7" rx="1" fill="var(--text-dark)"/><path d="M1.5 3l4.5 3.5L10.5 3" stroke="var(--band-teal)" fill="none"/></svg>mkdelgado1@inbox-example.com</li>
    <li><svg class="icon" viewBox="0 0 12 12"><circle cx="6" cy="6" r="5" fill="none" stroke="var(--text-dark)" stroke-width="1.2"/><path d="M1 6h10M6 1c2 2 2 8 0 10M6 1c-2 2-2 8 0 10" stroke="var(--text-dark)" fill="none"/></svg>www.oakharborrehabilitation-example.com</li>
  </ul>
</section>

</body>
</html>
```